Quorvane Power Point Template - Institutional Presentation

Develop a comprehensive template for a corporate presentation power point.

The presentation will be aimed to institutional investors.

Style to be modern and contemporary. Use of icons and images welcome but not to much.

It would be great if you could develop the layout/style for the content in the following slides:

- Cover
- Section title
- Slide with title and bullet points on one side and two text boxes on the other side
- Slide with line chart and pie chart
- Slide with table

Should we like the slides above we will then develop the rest of the template.

We may then need to have a dark-background version - but this will be invoiced separately.

Target Market(s)

Corporate institutional investors

Industry/Entity Type

Finance

Font styles to use
Serif
Sans Serif

Colors
3176b5
0255a3
cee9f5
86cae7
33a6d7
0792cd
33b8a4
00a990
86cfc6

Requirements
Must have
• Mostly white background with minimal objects
Nice to have
• Use of photos, but not to much.

```html
<!DOCTYPE html>
<html lang="en">
<head>
<meta charset="utf-8">
<title>Quorvane Pitch Deck</title>
<link rel="stylesheet" href="https://fonts.googleapis.com/css2?family=Montserrat:wght@400;600;700&family=Lato:wght@300;400;700&display=swap">
<style>
:root{
  --board:#474747;
  --white:#ffffff;
  --navy:#1f3557;
  --blue:#0255a3;
  --blue-mid:#3176b5;
  --sky:#0792cd;
  --sky-2:#33a6d7;
  --sky-light:#86cae7;
  --ice:#cee9f5;
  --teal:#00a990;
  --teal-2:#33b8a4;
  --teal-light:#86cfc6;
  --orange:#f39c12;
  --green:#8cc152;
  --slate:#5f7585;
  --text:#7a828a;
  --rule:#dfe5ea;
}
*{box-sizing:border-box;margin:0;padding:0}
html,body{width:1200px;height:624px;overflow:hidden}
body{background:var(--board);position:relative;font-family:"Lato",sans-serif;color:var(--text)}
.slide{position:absolute;width:262px;height:149px;background:var(--white);overflow:hidden}
.abs{position:absolute}
.kicker{position:absolute;left:0;right:0;top:6px;text-align:center;font:400 3px/1 "Montserrat",sans-serif;letter-spacing:.3px;color:#9aa3ab}
.title{position:absolute;left:0;right:0;top:11px;text-align:center;font:400 7px/1 "Montserrat",sans-serif;color:var(--blue-mid)}
.page{position:absolute;right:10px;top:8px;width:8px;height:8px;border:0.6px solid #b5bcc3;border-radius:50%;font:400 2.6px/7px "Lato",sans-serif;text-align:center;color:#9aa3ab}
.footer{position:absolute;left:14px;right:14px;bottom:5px;height:8px;border-top:0.6px solid var(--rule);padding-top:3px;display:flex;align-items:center;gap:3px}
.footer .brand{background:var(--navy);color:var(--white);font:700 3.6px/1 "Montserrat",sans-serif;padding:1.2px 2.5px;letter-spacing:.2px}
.footer .deck{font:400 3.4px/1 "Montserrat",sans-serif;color:#7a828a}
.body-s{font:300 3.3px/5.2px "Lato",sans-serif;color:var(--text)}
.photo{position:absolute}

.cover-photo{left:0;top:0;width:262px;height:92px;background:linear-gradient(160deg,#cfe0ee 0%,#7f9ab3 40%,#3d5670 75%,#203248 100%)}
.cover-name{left:60px;top:62px;width:138px;height:40px;background:var(--navy);color:var(--white);font:700 19px/40px "Montserrat",sans-serif;text-align:center;letter-spacing:1.5px}
.cover-sub{left:0;right:0;top:113px;text-align:center;font:400 6.5px/1 "Montserrat",sans-serif;color:var(--blue-mid);letter-spacing:.3px}
.cover-stripes{left:0;right:0;bottom:0;height:5px;display:flex}
.cover-stripes span{flex:1}

.agenda-item{position:absolute;display:flex;gap:4px;width:100px}
.agenda-icon{width:8px;height:8px;flex:none;display:flex;align-items:center;justify-content:center}
.agenda-label{font:400 4.6px/1 "Montserrat",sans-serif;color:var(--blue-mid)}
.agenda-note{font:300 2.6px/1.2 "Lato",sans-serif;color:var(--text);margin-top:1.3px}

.hero-photo{left:0;top:0;width:262px;height:149px}
.hero-title{position:absolute;right:14px;bottom:20px;font:700 15px/1 "Montserrat",sans-serif;color:var(--white);text-align:right}
.hero-sub{position:absolute;right:14px;bottom:13px;font:700 4px/1 "Montserrat",sans-serif;color:var(--white);letter-spacing:.2px}
.hero-icon{position:absolute;right:9px;top:7px}

.element{position:absolute;left:18px;display:flex;gap:5px;width:105px}
.element-num{width:10px;height:10px;border:0.7px solid #aab3bb;border-radius:50%;flex:none;font:400 4px/9px "Montserrat",sans-serif;text-align:center;color:#8a939b}
.element-title{font:400 4px/1 "Montserrat",sans-serif;color:#5b6670}
.element-note{font:300 2.8px/3.6px "Lato",sans-serif;color:var(--text);margin-top:1px}

.org-top{left:108px;top:26px;width:46px;height:9px;background:var(--sky);color:var(--white);font:400 3.8px/9px "Montserrat",sans-serif;text-align:center}
.dept{position:absolute;top:53px;width:46px}
.dept-head{height:9px;color:var(--white);font:400 3.6px/9px "Montserrat",sans-serif;text-align:center}
.dept-box{height:48px;padding:4px 3px;font:300 3px/4.2px "Lato",sans-serif;color:#6f7780;text-align:center}

.bullet{position:absolute;left:22px;width:220px}
.bullet-head{display:flex;align-items:center;gap:3px;font:400 4px/1 "Montserrat",sans-serif;color:#5b6670}

.port-head{left:16px;top:32px;width:82px;font:300 7px/8.5px "Lato",sans-serif;color:#4a5560}

.member{position:absolute;top:22px;width:60px;text-align:center}
.member-photo{width:44px;height:44px;border-radius:50%;margin:0 auto;border:1.5px solid #e4e8ec}
.member-name{font:400 5px/1 "Montserrat",sans-serif;margin-top:5px}
.member-note{font:300 2.8px/3.6px "Lato",sans-serif;color:var(--text);margin:2px auto 0;width:46px}
.socials{display:flex;justify-content:center;gap:2px;margin-top:4px}
.socials span{width:5px;height:5px;border:0.5px solid #aab3bb;border-radius:50%}
</style>
</head>
<body>

<section class="slide" style="left:47px;top:43px">
  <div class="photo cover-photo" role="img" aria-label="Upward view of glass office towers against a pale sky"></div>
  <div class="abs cover-name">QUORVANE</div>
  <div class="abs cover-sub">PRESENTATION PITCH DECK</div>
  <div class="abs cover-stripes">
    <span style="background:var(--blue)"></span><span style="background:var(--sky)"></span><span style="background:var(--blue-mid)"></span><span style="background:var(--sky-2)"></span><span style="background:var(--navy)"></span><span style="background:var(--teal-light)"></span><span style="background:var(--teal)"></span>
  </div>
</section>

<section class="slide" style="left:325px;top:43px">
  <div class="kicker">WRITE HERE A TITLE</div>
  <div class="title">Our Agenda for Today</div>
  <div class="page">02</div>
  <div class="agenda-item" style="left:30px;top:31px"><div class="agenda-icon" style="background:var(--sky)"></div><div><div class="agenda-label">About Us</div><div class="agenda-note">Short note about this topic</div></div></div>
  <div class="agenda-item" style="left:30px;top:50px"><div class="agenda-icon" style="background:var(--slate)"></div><div><div class="agenda-label">Our Works</div><div class="agenda-note">Short note about this topic</div></div></div>
  <div class="agenda-item" style="left:30px;top:69px"><div class="agenda-icon" style="background:var(--teal-2)"></div><div><div class="agenda-label">Knowing the Problem</div><div class="agenda-note">Short note about this topic</div></div></div>
  <div class="agenda-item" style="left:30px;top:88px"><div class="agenda-icon" style="background:var(--orange)"><svg width="5" height="5" viewBox="0 0 5 5"><path d="M.6 2.6 L2 4 L4.5 1" stroke="#fff" stroke-width=".8" fill="none"/></svg></div><div><div class="agenda-label">The Solution</div><div class="agenda-note">Short note about this topic</div></div></div>
  <div class="agenda-item" style="left:30px;top:107px"><div class="agenda-icon" style="background:var(--green)"></div><div><div class="agenda-label">Business Model</div><div class="agenda-note">Short note about this topic</div></div></div>
  <div class="agenda-item" style="left:148px;top:31px"><div class="agenda-icon" style="background:var(--green)"></div><div><div class="agenda-label">Marketing Plan</div><div class="agenda-note">Short note about this topic</div></div></div>
  <div class="agenda-item" style="left:148px;top:50px"><div class="agenda-icon" style="background:var(--green)"></div><div><div class="agenda-label">Competitor Analysis</div><div class="agenda-note">Short note about this topic</div></div></div>
  <div class="agenda-item" style="left:148px;top:69px"><div class="agenda-icon" style="background:var(--orange)"></div><div><div class="agenda-label">Management Team</div><div class="agenda-note">Short note about this topic</div></div></div>
  <div class="agenda-item" style="left:148px;top:88px"><div class="agenda-icon" style="background:var(--teal-2)"></div><div><div class="agenda-label">Financial Projections</div><div class="agenda-note">Short note about this topic</div></div></div>
  <div class="agenda-item" style="left:148px;top:107px"><div class="agenda-icon" style="background:var(--slate)"></div><div><div class="agenda-label">Accomplishments</div><div class="agenda-note">Short note about this topic</div></div></div>
  <div class="footer"><span class="brand">QUORVANE</span><span class="deck">PITCH DECK</span></div>
</section>

<section class="slide" style="left:604px;top:43px">
  <div class="photo hero-photo" role="img" aria-label="Team of smiling business professionals standing together" style="background:linear-gradient(100deg,#dcdfe2 0%,#b9bfc5 45%,#8f9aa5 100%)"></div>
  <svg class="abs" style="left:0;top:0" width="262" height="149" viewBox="0 0 262 149">
    <polygon points="150,0 262,0 262,149 95,149" fill="#0792cd" opacity=".55"/>
    <polygon points="190,0 262,0 262,149 150,149" fill="#0255a3" opacity=".45"/>
  </svg>
  <svg class="hero-icon" width="10" height="10" viewBox="0 0 10 10"><path d="M1 5 L5 1.5 L9 5 L8 5 L8 9 L6 9 L6 6.5 L4 6.5 L4 9 L2 9 L2 5 Z" fill="#fff"/></svg>
  <div class="hero-title">ABOUT US</div>
  <div class="hero-sub">PRESENTED BY: NAME HERE</div>
</section>

<section class="slide" style="left:880px;top:43px">
  <div class="kicker">WRITE HERE A TITLE</div>
  <div class="title">Inside of our Company</div>
  <div class="page">04</div>
  <div class="element" style="top:28px"><div class="element-num">1</div><div><div class="element-title">Element One</div><div class="element-note">Short line of text about this element goes here.</div></div></div>
  <div class="element" style="top:51px"><div class="element-num">2</div><div><div class="element-title">Element Two</div><div class="element-note">Short line of text about this element goes here.</div></div></div>
  <div class="element" style="top:74px"><div class="element-num">3</div><div><div class="element-title">Element Three</div><div class="element-note">Short line of text about this element goes here.</div></div></div>
  <div class="element" style="top:97px"><div class="element-num">4</div><div><div class="element-title">Element Four</div><div class="element-note">Short line of text about this element goes here.</div></div></div>
  <div class="photo" role="img" aria-label="Colleagues working together around a meeting table" style="left:133px;top:32px;width:116px;height:78px;background:linear-gradient(135deg,#c9d3da 0%,#8e9ca8 50%,#5e6d7a 100%)"></div>
  <div class="footer"><span class="brand">QUORVANE</span><span class="deck">PITCH DECK</span></div>
</section>

<section class="slide" style="left:47px;top:224px">
  <div class="kicker">WRITE HERE A TITLE</div>
  <div class="title">Organization Chart Sample</div>
  <div class="page">05</div>
  <div class="abs org-top">Management</div>
  <svg class="abs" style="left:0;top:0" width="262" height="60" viewBox="0 0 262 60">
    <path d="M131 35 V44 M50 44 H206 M50 44 V53 M102 44 V53 M154 44 V53 M206 44 V53" stroke="#9aa3ab" stroke-width=".6" fill="none"/>
  </svg>
  <div class="dept" style="left:27px"><div class="dept-head" style="background:var(--slate)">Department A</div><div class="dept-box" style="background:#eef1f4">Short note about this department and its role in the company.</div></div>
  <div class="dept" style="left:79px"><div class="dept-head" style="background:var(--teal-2)">Department B</div><div class="dept-box" style="background:#e6f5f2">Short note about this department and its role in the company.</div></div>
  <div class="dept" style="left:131px"><div class="dept-head" style="background:var(--blue-mid)">Department C</div><div class="dept-box" style="background:#e8f0f8">Short note about this department and its role in the company.</div></div>
  <div class="dept" style="left:183px"><div class="dept-head" style="background:var(--sky-2)">Department D</div><div class="dept-box" style="background:#e9f5fb">Short note about this department and its role in the company.</div></div>
  <p class="abs body-s" style="left:20px;top:117px;width:222px">Entrepreneurship is the process of starting a business and building a company with an idea that creates value for people.</p>
  <div class="footer"><span class="brand">QUORVANE</span><span class="deck">PITCH DECK</span></div>
</section>

<section class="slide" style="left:325px;top:224px">
  <div class="kicker">WRITE HERE A TITLE</div>
  <div class="title">Full Width Text Sample</div>
  <div class="page">06</div>
  <p class="abs body-s" style="left:20px;top:27px;width:222px">Entrepreneurship is the process of starting a business and building a company with an idea that creates value for people. Entrepreneurship is the process of starting a business and building a company with an idea that creates value for people. Entrepreneurship is the process of starting a business and building a company with an idea that creates value for people. Entrepreneurship is the process of starting a business and building a company with an idea that creates value for people. Entrepreneurship is the process of starting a business and building a company with an idea that creates value for people. Entrepreneurship is the process of starting a business and building a company with an idea that creates value for people.</p>
  <p class="abs body-s" style="left:20px;top:67px;width:222px">Entrepreneurship is the process of starting a business and building a company with an idea that creates value for people. Entrepreneurship is the process of starting a business and building a company with an idea that creates value for people. Entrepreneurship is the process of starting a business and building a company with an idea that creates value for people. Entrepreneurship is the process of starting a business and building a company with an idea that creates value for people. Entrepreneurship is the process of starting a business and building a company with an idea that creates value for people. Entrepreneurship is the process of starting a business and building a company with an idea that creates value for people. Entrepreneurship is the process of starting a business and building a company with an idea that creates value for people.</p>
  <div class="footer"><span class="brand">QUORVANE</span><span class="deck">PITCH DECK</span></div>
</section>

<section class="slide" style="left:604px;top:224px">
  <div class="kicker">WRITE HERE A TITLE</div>
  <div class="title">Two Columns Text Sample</div>
  <div class="page">07</div>
  <p class="abs body-s" style="left:20px;top:25px;width:222px;height:99px;column-count:2;column-gap:12px;overflow:hidden">Entrepreneurship is the process of starting a business and building a company with an idea that creates value for people. Entrepreneurship is the process of starting a business and building a company with an idea that creates value for people. Entrepreneurship is the process of starting a business and building a company with an idea that creates value for people. Entrepreneurship is the process of starting a business and building a company with an idea that creates value for people. Entrepreneurship is the process of starting a business and building a company with an idea that creates value for people. Entrepreneurship is the process of starting a business and building a company with an idea that creates value for people. Entrepreneurship is the process of starting a business and building a company with an idea that creates value for people. Entrepreneurship is the process of starting a business and building a company with an idea that creates value for people. Entrepreneurship is the process of starting a business and building a company with an idea that creates value for people. Entrepreneurship is the process of starting a business and building a company with an idea that creates value for people. Entrepreneurship is the process of starting a business and building a company with an idea that creates value for people. Entrepreneurship is the process of starting a business and building a company with an idea that creates value for people. Entrepreneurship is the process of starting a business and building a company with an idea that creates value for people. Entrepreneurship is the process of starting a business and building a company with an idea that creates value for people. Entrepreneurship is the process of starting a business and building a company with an idea that creates value for people. Entrepreneurship is the process of starting a business and building a company with an idea that creates value for people. Entrepreneurship is the process of starting a business and building a company with an idea that creates value for people. Entrepreneurship is the process of starting a business and building a company with an idea.</p>
  <div class="footer"><span class="brand">QUORVANE</span><span class="deck">PITCH DECK</span></div>
</section>

<section class="slide" style="left:880px;top:224px">
  <div class="kicker">WRITE HERE A TITLE</div>
  <div class="title">Bulleted List Text Sample</div>
  <div class="page">08</div>
  <div class="bullet" style="top:29px"><div class="bullet-head"><svg width="5" height="5" viewBox="0 0 5 5"><path d="M.6 2.6 L2 4 L4.5 1" stroke="#33b8a4" stroke-width=".8" fill="none"/></svg>Your First Title goes here</div><p class="body-s" style="margin-top:1.5px">Entrepreneurship is the process of starting a business and building a company with an idea that creates value for people. It offers new products and services to the market.</p></div>
  <div class="bullet" style="top:52px"><div class="bullet-head"><svg width="5" height="5" viewBox="0 0 5 5"><path d="M.6 2.6 L2 4 L4.5 1" stroke="#33b8a4" stroke-width=".8" fill="none"/></svg>Your Second Title goes here</div><p class="body-s" style="margin-top:1.5px">Entrepreneurship is the process of starting a business and building a company with an idea that creates value for people. It offers new products and services to the market.</p></div>
  <div class="bullet" style="top:75px"><div class="bullet-head"><svg width="5" height="5" viewBox="0 0 5 5"><path d="M.6 2.6 L2 4 L4.5 1" stroke="#33b8a4" stroke-width=".8" fill="none"/></svg>Your Third Title goes here</div><p class="body-s" style="margin-top:1.5px">Entrepreneurship is the process of starting a business and building a company with an idea that creates value for people. It offers new products and services to the market.</p></div>
  <div class="bullet" style="top:98px"><div class="bullet-head"><svg width="5" height="5" viewBox="0 0 5 5"><path d="M.6 2.6 L2 4 L4.5 1" stroke="#33b8a4" stroke-width=".8" fill="none"/></svg>Your Fourth Title goes here</div><p class="body-s" style="margin-top:1.5px">Entrepreneurship is the process of starting a business and building a company with an idea that creates value for people. It offers new products and services to the market.</p></div>
  <div class="footer"><span class="brand">QUORVANE</span><span class="deck">PITCH DECK</span></div>
</section>

<section class="slide" style="left:47px;top:420px">
  <div class="photo hero-photo" role="img" aria-label="Group of business people smiling in an office" style="background:linear-gradient(100deg,#8fa3b8 0%,#c4ccd4 45%,#e2e5e8 100%)"></div>
  <svg class="abs" style="left:0;top:0" width="262" height="149" viewBox="0 0 262 149">
    <polygon points="170,0 262,0 262,149 120,149" fill="#3a4a5c" opacity=".35"/>
  </svg>
  <svg class="hero-icon" width="11" height="10" viewBox="0 0 11 10"><rect x="1" y="3" width="9" height="6" fill="#fff"/><path d="M4 3 V1.5 H7 V3" stroke="#fff" stroke-width=".9" fill="none"/></svg>
  <div class="hero-title">OUR WORKS</div>
  <div class="hero-sub">PRESENTED BY: NAME HERE</div>
</section>

<section class="slide" style="left:325px;top:420px">
  <div class="kicker">WRITE HERE A TITLE</div>
  <div class="title">Portfolio Showcase</div>
  <div class="page">10</div>
  <div class="abs port-head">International Project for an important company.</div>
  <p class="abs body-s" style="left:16px;top:55px;width:82px">Entrepreneurship is the process of starting a business and building a company with an idea that creates value for people. Entrepreneurship is the process of starting a business and building a company with an idea that creates value for people.</p>
  <div class="photo" role="img" aria-label="Collage of project photos showing office teams at work" style="left:103px;top:33px;width:145px;height:78px;background:linear-gradient(120deg,#d5dbe0 0%,#9aa8b4 50%,#6b7a88 100%)"></div>
  <div class="footer"><span class="brand">QUORVANE</span><span class="deck">PITCH DECK</span></div>
</section>

<section class="slide" style="left:604px;top:420px">
  <div class="kicker">WRITE HERE A TITLE</div>
  <div class="title">Meet our Dedicated Team</div>
  <div class="page">11</div>
  <div class="member" style="left:12px"><div class="member-photo" role="img" aria-label="Portrait of team member" style="background:linear-gradient(160deg,#c9ced3,#8d969e)"></div><div class="member-name" style="color:var(--blue-mid)">Owen Reyes</div><div class="member-note">Short note about this team member here.</div><div class="socials"><span></span><span></span><span></span></div></div>
  <div class="member" style="left:71px"><div class="member-photo" role="img" aria-label="Portrait of team member" style="background:linear-gradient(160deg,#d4d8dc,#98a1a9)"></div><div class="member-name" style="color:#5b6670">Kai Pinto</div><div class="member-note">Short note about this team member here.</div><div class="socials"><span></span><span></span><span></span></div></div>
  <div class="member" style="left:132px"><div class="member-photo" role="img" aria-label="Portrait of team member" style="background:linear-gradient(160deg,#d6d9dc,#a0a8ae)"></div><div class="member-name" style="color:var(--teal-2)">Clara Ellis</div><div class="member-note">Short note about this team member here.</div><div class="socials"><span></span><span></span><span></span></div></div>
  <div class="member" style="left:195px"><div class="member-photo" role="img" aria-label="Portrait of team member" style="background:linear-gradient(160deg,#cfd3d7,#949da5)"></div><div class="member-name" style="color:var(--orange)">Mark Soto</div><div class="member-note">Short note about this team member here.</div><div class="socials"><span></span><span></span><span></span></div></div>
  <div class="footer"><span class="brand">QUORVANE</span><span class="deck">PITCH DECK</span></div>
</section>

<section class="slide" style="left:880px;top:420px">
  <div class="kicker">WRITE HERE A TITLE</div>
  <div class="title">Comparison Diagram Analytics</div>
  <div class="page">12</div>
  <svg class="abs" style="left:0;top:0" width="262" height="110" viewBox="0 0 262 110">
    <g stroke="#e6eaee" stroke-width=".4">
      <path d="M30 36 H128 M30 48 H128 M30 60 H128 M30 72 H128 M30 84 H128"/>
      <path d="M145 38 H240 M145 50 H240 M145 62 H240 M145 74 H240 M145 86 H240"/>
    </g>
    <rect x="30" y="36" width="88" height="3" fill="#33b8a4"/>
    <rect x="30" y="40" width="70" height="3" fill="#3176b5"/>
    <rect x="30" y="48" width="62" height="3" fill="#86cfc6"/>
    <rect x="30" y="52" width="98" height="3" fill="#1f3557"/>
    <rect x="30" y="60" width="50" height="3" fill="#33b8a4"/>
    <rect x="30" y="64" width="80" height="3" fill="#3176b5"/>
    <rect x="30" y="72" width="74" height="3" fill="#86cfc6"/>
    <rect x="30" y="76" width="40" height="3" fill="#1f3557"/>
    <path d="M30 33 V86" stroke="#b5bcc3" stroke-width=".5"/>
    <path d="M145 34 V88 H240" stroke="#b5bcc3" stroke-width=".5" fill="none"/>
    <polyline points="150,70 168,62 186,60 204,54 222,48 238,40" fill="none" stroke="#3176b5" stroke-width=".8"/>
    <polyline points="150,62 168,64 186,58 204,63 222,60 238,58" fill="none" stroke="#1f3557" stroke-width=".8"/>
    <polyline points="150,80 168,76 186,70 204,72 222,66 238,66" fill="none" stroke="#86cae7" stroke-width=".8"/>
  </svg>
  <p class="abs body-s" style="left:28px;top:100px;width:208px">Entrepreneurship is the process of starting a business and building a company with an idea that creates value for people. It offers new products and services to the market.</p>
  <div class="footer"><span class="brand">QUORVANE</span><span class="deck">PITCH DECK</span></div>
</section>

</body>
</html>
```